Business Card for a Jewellery Brand

Business card for an upscale jewellery brand. Attached is the brand logo and icon and color board. I am looking for two card versions: one for the founder and one is generic. The card should be elegant and convey upscale and premium feel. I am open to both square and rectangle card shapes.

Industry/Entity Type

Jewelry

Contact Information for Business Card

Two cards: (1) Sunila Perumbadi (Founder) (2) General
(1) Sunila Perumbadi card should have Name: Sunila Perumbadi, Title: Founder Email id: sunila@quelm.com.au. Phone no: +61412555307
(2) Generic card should have Email id: info@quelm.com.au. Phone no: +61431555962

Requirements
Must have
• Workmark
• ICON
• Phone no
• Email ID
• ABN: 48917205563 (Note: ABN is Business number in Australia)
• Website: www.quelm.com.au
• Instagram: quelm_jewellery
• Facebook: @quelmjewellery
Nice to have
• Tagline

```html
<!DOCTYPE html>
<html lang="en">
<head>
<meta charset="utf-8">
<title>QUELM Business Card</title>
<link rel="stylesheet" href="https://fonts.googleapis.com/css2?family=Roboto:wght@300;400&family=Roboto+Condensed:wght@400;700&display=swap">
<style>
  :root {
    --backdrop: #e4e4e4;
    --card-white: #f3f3f3;
    --rose: #dc8f8c;
    --rose-light: #e39c99;
    --rose-deep: #d7827f;
    --ink: #3d3d3d;
    --white: #ffffff;
  }
  * { margin: 0; padding: 0; box-sizing: border-box; }
  html, body {
    width: 1200px;
    height: 960px;
    overflow: hidden;
    background: var(--backdrop);
  }
  .canvas {
    position: relative;
    width: 1200px;
    height: 960px;
    font-family: "Roboto", Arial, sans-serif;
  }
  .card {
    position: absolute;
    width: 600px;
    height: 343px;
    overflow: hidden;
  }

  /* Front */
  .card-front {
    left: 302px;
    top: 129px;
    background: var(--card-white);
  }
  .name-band {
    position: absolute;
    left: 0;
    top: 43px;
    width: 100%;
    height: 70px;
    background: var(--rose);
  }
  .person-name {
    position: absolute;
    left: 34px;
    top: 13px;
    font-family: "Roboto Condensed", "Arial Narrow", sans-serif;
    font-weight: 700;
    font-size: 21px;
    color: var(--white);
    letter-spacing: 0.2px;
  }
  .person-title {
    position: absolute;
    left: 34px;
    top: 39px;
    font-family: "Roboto Condensed", "Arial Narrow", sans-serif;
    font-weight: 400;
    font-size: 15px;
    color: var(--white);
  }
  .brand-mark {
    position: absolute;
    left: 446px;
    top: 50px;
    width: 64px;
    height: 64px;
    border-radius: 50%;
    background: var(--card-white);
    border: 3px solid var(--rose);
  }
  .brand-name {
    position: absolute;
    right: 36px;
    top: 137px;
    font-family: "Roboto", Arial, sans-serif;
    font-weight: 300;
    font-size: 44px;
    letter-spacing: 9px;
    margin-right: -9px;
    color: var(--rose);
    line-height: 1;
  }
  .contact-list {
    position: absolute;
    left: 36px;
    top: 238px;
    list-style: none;
  }
  .contact-list li {
    display: flex;
    align-items: center;
    height: 18px;
    font-size: 14.5px;
    color: var(--ink);
  }
  .contact-icon {
    width: 12px;
    height: 12px;
    margin-right: 8px;
    flex: none;
  }
  .business-details {
    position: absolute;
    right: 36px;
    top: 274px;
    text-align: right;
    font-size: 14.5px;
    color: var(--ink);
    line-height: 19px;
  }

  /* Back */
  .card-back {
    left: 299px;
    top: 488px;
  }
  .back-field {
    position: absolute;
    inset: 0;
    background: linear-gradient(135deg, var(--rose-light) 0%, var(--rose) 50%, var(--rose-deep) 100%);
  }
  .back-mark {
    position: absolute;
    left: 480px;
    top: 212px;
    width: 32px;
    height: 32px;
    border-radius: 50%;
    border: 3px solid var(--white);
  }
  .back-brand {
    position: absolute;
    left: 396px;
    width: 200px;
    top: 250px;
    text-align: center;
    font-family: "Roboto", Arial, sans-serif;
    font-weight: 300;
    font-size: 26px;
    line-height: 1;
    letter-spacing: 7px;
    text-indent: 7px;
    color: var(--white);
  }
  .tagline {
    position: absolute;
    left: 396px;
    width: 200px;
    top: 297px;
    text-align: center;
    font-size: 14px;
    font-weight: 400;
    color: var(--white);
    letter-spacing: 0.3px;
  }
</style>
</head>
<body>
<main class="canvas">

  <section class="card card-front" aria-label="Business card front">
    <div class="name-band">
      <h1 class="person-name">Sunila Perumbadi</h1>
      <p class="person-title">Founder</p>
    </div>

    <div class="brand-mark" aria-hidden="true"></div>
    <div class="brand-name">QUELM</div>

    <ul class="contact-list">
      <li>
        <svg class="contact-icon" viewBox="0 0 12 12" aria-hidden="true">
          <rect x="3" y="0.5" width="6" height="11" rx="1" fill="none" stroke="#dc8f8c" stroke-width="1.2"/>
          <line x1="5" y1="9.6" x2="7" y2="9.6" stroke="#dc8f8c" stroke-width="1"/>
        </svg>
        +61412555307
      </li>
      <li>
        <svg class="contact-icon" viewBox="0 0 12 12" aria-hidden="true">
          <rect x="0.6" y="2.5" width="10.8" height="7.5" fill="none" stroke="#dc8f8c" stroke-width="1.1"/>
          <polyline points="0.8,2.8 6,7 11.2,2.8" fill="none" stroke="#dc8f8c" stroke-width="1.1"/>
        </svg>
        sunila@quelm.com.au
      </li>
      <li>
        <svg class="contact-icon" viewBox="0 0 12 12" aria-hidden="true">
          <rect x="1" y="1" width="10" height="10" fill="#dc8f8c"/>
        </svg>
        quelm_jewellery
      </li>
      <li>
        <svg class="contact-icon" viewBox="0 0 12 12" aria-hidden="true">
          <rect x="1" y="1" width="10" height="10" fill="#dc8f8c"/>
        </svg>
        @quelmjewellery
      </li>
    </ul>

    <div class="business-details">
      <p>ABN: 48917205563</p>
      <p>www.quelm.com.au</p>
    </div>
  </section>

  <section class="card card-back" aria-label="Business card back">
    <div class="back-field" role="img" aria-label="Repeating faint rose geometric pattern covering the whole card back"></div>
    <div class="back-mark" aria-hidden="true"></div>
    <div class="back-brand">QUELM</div>
    <p class="tagline">LOVE IS IN THE AIR</p>
  </section>

</main>
</body>
</html>
```